Flier redesign 2021

The 3 prior year fliers are attached. We want a new design for 2021 -

* DO NOT SIMPLY COPY and change the year.
*All text should be the same, except year is 2021.
*Use different photos. You can find photos on our website maplecrestgardens.org or on our google page.

Requirements
Must have
• MUST be done in photoshop an photoshop file must be provided at the end.
Should not have
• Should not be same design as previous years.

```html
<!DOCTYPE html>
<html lang="en">
<head>
<meta charset="utf-8">
<title>2021 Landscaping Packages – Maplecrest Gardens</title>
<link rel="stylesheet" href="https://fonts.googleapis.com/css2?family=Arimo:wght@700&family=Source+Sans+3:wght@400;600;700&family=Cinzel:wght@400;500&family=Noto+Serif:wght@400&display=swap">
<style>
  :root {
    --band: #5a1a0c;
    --header: #6a1f10;
    --header-dark: #561609;
    --burgundy: #7a2336;
    --ink: #1e1a1a;
    --card: #f9fbfb;
    --yellow: #fff200;
    --white: #ffffff;
    --shadow: rgba(0,0,0,0.45);
  }
  * { margin: 0; padding: 0; box-sizing: border-box; }
  html, body { width: 927px; height: 1200px; overflow: hidden; background: var(--white); }
  .flier { position: relative; width: 927px; height: 1200px; overflow: hidden; background: var(--white); font-family: "Source Sans 3", sans-serif; color: var(--ink); }

  .top-band { position: absolute; left: 0; top: 0; width: 927px; height: 94px; background: var(--band); }
  .title { position: absolute; left: 49px; top: 20px; font-family: "Arimo", sans-serif; font-weight: 700; font-size: 44px; letter-spacing: 1px; color: var(--white); line-height: 1; }

  .hero { position: absolute; left: 0; top: 94px; width: 927px; height: 530px;
    background: linear-gradient(180deg, #8fb3d9 0%, #c9d9ea 35%, #b9c4c6 55%, #b8672c 68%, #c9843c 78%, #d8d2c8 86%, #ffffff 100%); }
  .hero-fade { position: absolute; left: 0; top: 500px; width: 927px; height: 130px; background: linear-gradient(180deg, rgba(255,255,255,0) 0%, #ffffff 100%); }

  .brand-badge { position: absolute; left: 775px; top: 0; width: 128px; height: 169px; background: var(--white); border-radius: 0 0 64px 64px; display: flex; flex-direction: column; align-items: center; justify-content: center; gap: 8px; }
  .brand-dot { width: 40px; height: 40px; border-radius: 50%; background: #e6e2dd; }
  .brand-name { font-family: "Noto Serif", serif; font-weight: 400; font-size: 17px; color: var(--burgundy); text-align: center; line-height: 1.1; }

  .popular-tab { position: absolute; left: 100px; top: 511px; width: 227px; height: 37px; background: var(--yellow); border-radius: 60px 60px 0 0 / 30px 30px 0 0; font-family: "Arimo", sans-serif; font-weight: 700; font-size: 11.5px; line-height: 12.5px; text-align: center; padding-top: 9px; color: #111; }

  .card { position: absolute; background: var(--card); box-shadow: 0 4px 3px -1px var(--shadow); }
  .card-head { background: linear-gradient(180deg, var(--header) 0%, var(--header-dark) 100%); color: var(--white); font-family: "Arimo", sans-serif; font-weight: 700; font-size: 24px; text-align: center; display: flex; align-items: center; justify-content: center; line-height: 29px; letter-spacing: 0.5px; }
  .card-lede { position: absolute; color: var(--burgundy); font-weight: 700; font-size: 19px; line-height: 25px; }
  .features { list-style: none; }
  .feature { position: absolute; font-size: 15px; line-height: 16.5px; padding-left: 32px; }
  .feature svg { position: absolute; left: 0; top: 0; width: 22px; height: 22px; }

  .perpetual { left: 23px; top: 548px; width: 380px; height: 581px; }
  .perpetual .card-head { height: 88px; }
  .basic { left: 415px; top: 548px; width: 487px; height: 303px; }
  .basic .card-head { height: 76px; }
  .seasonal { left: 415px; top: 871px; width: 487px; height: 258px; }
  .seasonal .card-head { height: 77px; }

  .price-label { font-family: "Cinzel", serif; color: var(--burgundy); font-weight: 500; }
  .price-amount { font-family: "Cinzel", serif; color: var(--burgundy); font-weight: 500; }
  .note { font-family: "Noto Serif", serif; color: var(--ink); text-align: center; }

  .perpetual .price-label { position: absolute; left: 30px; top: 456px; font-size: 22px; line-height: 25px; }
  .perpetual .price-amount { position: absolute; left: 212px; top: 448px; font-size: 58px; line-height: 64px; }
  .perpetual .note { position: absolute; left: 0; top: 525px; width: 380px; font-size: 16px; line-height: 19px; letter-spacing: 0.3px; }

  .basic .price-box { position: absolute; left: 300px; top: 169px; width: 175px; text-align: center; }
  .basic .price-label { font-size: 17px; line-height: 20px; display: block; }
  .basic .price-amount { font-size: 35px; line-height: 42px; display: block; font-weight: 500; }
  .basic .note { font-size: 9px; line-height: 11px; }

  .rates { position: absolute; left: 318px; top: 131px; }
  .rate { display: flex; align-items: baseline; height: 28px; }
  .rate .price-label { width: 91px; font-size: 18px; }
  .rate .price-amount { font-size: 25px; font-weight: 500; }
  .seasonal .note { position: absolute; right: 16px; top: 224px; font-size: 8.5px; line-height: 10.5px; text-align: right; }

  .footer { position: absolute; left: 0; top: 1151px; width: 927px; height: 49px; background: var(--band); color: var(--white); font-family: "Arimo", sans-serif; font-weight: 400; font-size: 18px; display: flex; align-items: center; justify-content: center; gap: 26px; }
</style>
</head>
<body>
<main class="flier">
  <header class="top-band">
    <h1 class="title">2021 LANDSCAPING PACKAGES</h1>
  </header>

  <div class="hero" role="img" aria-label="Photograph of the cemetery grounds in autumn: rows of white headstones, a stone entrance gate and colourful maple trees under a cloudy blue sky"></div>
  <div class="hero-fade"></div>

  <div class="brand-badge">
    <span class="brand-dot"></span>
    <span class="brand-name">Maplecrest<br>Gardens</span>
  </div>

  <div class="popular-tab">MOST POPULAR<br>PACKAGE!</div>

  <section class="card perpetual">
    <h2 class="card-head">PERPETUAL CARE<br>ENDOWMENT</h2>
    <p class="card-lede" style="left:21px;top:114px;">Landscaping care forever for graves<br>with plantings.</p>
    <ul class="features">
      <li class="feature" style="left:21px;top:182px;width:350px;"><svg viewBox="0 0 22 22"><rect x="1" y="4" width="16" height="16" fill="none" stroke="#7a2336" stroke-width="2"/><path d="M5 11 L9 16 L20 2" fill="none" stroke="#7a2336" stroke-width="3"/></svg>Weeding and triming services on your gravasite approximately every 7 weeks during the growing season : mid-April through mid-October</li>
      <li class="feature" style="left:21px;top:264px;"><svg viewBox="0 0 22 22"><rect x="1" y="4" width="16" height="16" fill="none" stroke="#7a2336" stroke-width="2"/><path d="M5 11 L9 16 L20 2" fill="none" stroke="#7a2336" stroke-width="3"/></svg>Monument leveling and cleaning</li>
      <li class="feature" style="left:21px;top:297px;"><svg viewBox="0 0 22 22"><rect x="1" y="4" width="16" height="16" fill="none" stroke="#7a2336" stroke-width="2"/><path d="M5 11 L9 16 L20 2" fill="none" stroke="#7a2336" stroke-width="3"/></svg>Payment ensures grave care forever</li>
      <li class="feature" style="left:21px;top:330px;"><svg viewBox="0 0 22 22"><rect x="1" y="4" width="16" height="16" fill="none" stroke="#7a2336" stroke-width="2"/><path d="M5 11 L9 16 L20 2" fill="none" stroke="#7a2336" stroke-width="3"/></svg>Full bed of boxwood shrubs</li>
      <li class="feature" style="left:21px;top:364px;"><svg viewBox="0 0 22 22"><rect x="1" y="4" width="16" height="16" fill="none" stroke="#7a2336" stroke-width="2"/><path d="M5 11 L9 16 L20 2" fill="none" stroke="#7a2336" stroke-width="3"/></svg>Replacement of shurbs</li>
      <li class="feature" style="left:21px;top:397px;"><svg viewBox="0 0 22 22"><rect x="1" y="4" width="16" height="16" fill="none" stroke="#7a2336" stroke-width="2"/><path d="M5 11 L9 16 L20 2" fill="none" stroke="#7a2336" stroke-width="3"/></svg>Trust certificate</li>
    </ul>
    <p class="price-label">12 MONTHLY<br>PAYMENTS OF</p>
    <p class="price-amount">$313</p>
    <p class="note">Call for single payment discount.<br>Valid through 10/31/2021</p>
  </section>

  <section class="card basic">
    <h2 class="card-head">BASIC CARE ENDOWMENT</h2>
    <p class="card-lede" style="left:21px;top:89px;">Landscaping care forever for graves<br>with no plantings.</p>
    <ul class="features">
      <li class="feature" style="left:21px;top:154px;width:275px;"><svg viewBox="0 0 22 22"><rect x="1" y="4" width="16" height="16" fill="none" stroke="#7a2336" stroke-width="2"/><path d="M5 11 L9 16 L20 2" fill="none" stroke="#7a2336" stroke-width="3"/></svg>Weeding and triming services on your gravasite 2 times per years : mid-May and mid-September</li>
      <li class="feature" style="left:21px;top:218px;"><svg viewBox="0 0 22 22"><rect x="1" y="4" width="16" height="16" fill="none" stroke="#7a2336" stroke-width="2"/><path d="M5 11 L9 16 L20 2" fill="none" stroke="#7a2336" stroke-width="3"/></svg>Monument leveling</li>
      <li class="feature" style="left:21px;top:252px;width:250px;"><svg viewBox="0 0 22 22"><rect x="1" y="4" width="16" height="16" fill="none" stroke="#7a2336" stroke-width="2"/><path d="M5 11 L9 16 L20 2" fill="none" stroke="#7a2336" stroke-width="3"/></svg>Payment ensures grave care forever</li>
    </ul>
    <div class="price-box">
      <span class="price-label">12 MONTHLY<br>PAYMENT OF</span>
      <span class="price-amount">$255</span>
      <p class="note">Call for single payment discount.<br>Valid through 10/31/2021</p>
    </div>
  </section>

  <section class="card seasonal">
    <h2 class="card-head">SEASONAL CARE</h2>
    <p class="card-lede" style="left:25px;top:93px;">Seasonal landscaping grave care.</p>
    <ul class="features">
      <li class="feature" style="left:25px;top:128px;width:270px;"><svg viewBox="0 0 22 22"><rect x="1" y="4" width="16" height="16" fill="none" stroke="#7a2336" stroke-width="2"/><path d="M5 11 L9 16 L20 2" fill="none" stroke="#7a2336" stroke-width="3"/></svg>Weeding and triming services on your gravasite approximately every 7 weeks during the growing season : mid-April through mid-October</li>
    </ul>
    <div class="rates">
      <div class="rate"><span class="price-label">3 YEARS</span><span class="price-amount">$357</span></div>
      <div class="rate"><span class="price-label">2 YEARS</span><span class="price-amount">$238</span></div>
      <div class="rate"><span class="price-label">1 YEARS</span><span class="price-amount">$119</span></div>
    </div>
    <p class="note">Multi-year payment locks in current rates.<br>Valid through 10/31/2021</p>
  </section>

  <footer class="footer">
    <span>(555) 214-3860</span><span>|</span><span>info@maplecrestgardens.org</span><span>|</span><span>maplecrestgardens.org</span>
  </footer>
</main>
</body>
</html>
```